Tamsin Vale Chiropractic Web Design

We need a fully operating Web site design INCLUDING the code for a Chiropractic Clinic based in Auckland New Zealand to target people from different financial backgrounds.

We need 4 Pages as followed:
1. Home: includes Slideshow of the clinic, General information about chiropractic, option for "Request an appointment", and it would be nice to have a picture on the top right side of the header and the clinic's name and logo on the top left side. on the bottom right we would like a small section for "Testimonial" (A good example: http://www.brindlemoorstudios.example/ )
(A good example for slide show is: http://www.pelvoro.example.nz/)
(A good example for the header is: http://www.spinehavenwelt.example.com/)

2. About Us: this section will include the background information of the company, and a section for our staff (which will includes a photo and description of each person/staff which can be changedanytime)
(a good example: http://www.fernwaybackcare.example.nz/)

3. Contact: includes location, map, contact numbers, email, and a contact box (A good example: http://www.brindlemoorstudios.example/contact/)

4. Services: includes our products, adjustment equipment, chiropractic products for sale, few pictures of patients while under chiropractic care/adjustment tables

We would also like to add "social networking" options on the bottom left side of every page (Facebook, twitter, Blog, Google+)

Please check the following links to get a feel of our favorite designs:
http://www.spinehavenwelt.example.com/
http://www.fernwaybackcare.example.nz/
http://www.pelvoro.example.nz/
http://www.dunmerespinalcentre.example.com/
http://www.quietbirch.example.nz/
http://www.pwo.example.nz/index-1.html
http://home.corelinespine.example.nz/home/

we would like to have full access to the back-end- admin of the website to be able to change and add any pictures or texts.
Updates

Hi Lovely Designer,

thank you so much for your proposed designs. We just uploaded the original source file of our logo, for you all to have access on it to facilitate your work. 

Enjoy your day

Leni

Target Market(s)

People with different financial background as well as we are located in the artistic part of town, so appealing to those crowd is important to us.

Industry/Entity Type

Financial

Requirements
Must have
• 1.color similar to the logo or darker colors (Dark and rich colors are prefered)
2. more artistic than a basic doctors' clinic
3. I would like the opening of the web to bring art, tranquility and peaceful images into mind
Should not have
• Not bombarded with lots of info and pics in one page, not too busy and crowded

```html
<!DOCTYPE html>
<html lang="en">
<head>
<meta charset="utf-8">
<title>Tamsin Vale Chiropractic</title>
<link rel="stylesheet" href="https://fonts.googleapis.com/css2?family=Questrial&family=Arimo:ital,wght@0,400;1,400&family=Open+Sans:wght@600;700&display=swap">
<style>
:root{
  --navy:#0e3a6b;
  --navy-deep:#0a2f59;
  --blue:#1b5a95;
  --title:#13406f;
  --green:#86b52a;
  --green-dark:#5f8f14;
  --green-light:#a2cb45;
  --lime:#b9d86a;
  --text:#222;
  --muted:#555;
  --footer:#1c1c1c;
  --footer-text:#8a8a8a;
  --star:#f08a2a;
}
*{box-sizing:border-box;margin:0;padding:0}
html,body{width:1029px;height:1200px;overflow:hidden}
body{position:relative;background:linear-gradient(#e9e9e9 225px,#f4f4f4 600px,#f7f7f7 900px,#ececec 1107px);font-family:"Arimo",Arial,sans-serif;color:var(--text)}
.abs{position:absolute}
h3,h4{font-weight:400}

/* header */
.site-header{left:0;top:0;width:1029px;height:185px;background:linear-gradient(100deg,var(--navy-deep) 0%,var(--blue) 55%,var(--navy) 100%)}
.brand{left:105px;top:44px;display:flex;align-items:center;gap:12px}
.brand-dot{width:14px;height:14px;border-radius:50%;background:var(--lime)}
.brand-name{font-family:"Questrial",sans-serif;color:#fff;font-size:27px;line-height:30px;letter-spacing:1px;white-space:nowrap}
.header-photo{left:598px;top:0;width:322px;height:185px;background:linear-gradient(180deg,#2d6aa3 0%,#c9b7a3 55%,#e8ddd3 100%)}

/* navigation */
.main-nav{left:0;top:185px;width:1029px;height:40px;background:linear-gradient(#95c233,#6c9c19)}
.main-nav ul{list-style:none;position:absolute;left:108px;top:0;height:40px;display:flex}
.main-nav li{font-family:"Questrial",sans-serif;font-size:16px;color:#fff;height:40px;line-height:40px;padding:0 22px;position:relative;letter-spacing:.3px;white-space:nowrap}
.main-nav li+li::before{content:"";position:absolute;left:0;top:10px;height:20px;width:1px;background:rgba(255,255,255,.45)}
.main-nav li.active{background:#a4cb47}
.main-nav li:nth-child(2){margin-left:14px}
.main-nav li:nth-child(3){margin-left:5px}
.main-nav li:nth-child(4){margin-left:9px}
.main-nav li:nth-child(5){margin-left:6px}

/* slider */
.slider{left:110px;top:241px;width:811px;height:350px;background:#fff;box-shadow:0 8px 10px -6px rgba(0,0,0,.35)}
.slide-photo{left:5px;top:5px;width:801px;height:338px;background:linear-gradient(90deg,#5ab8dc 0%,#7cc6df 28%,#e9e6e2 45%,#d9b79c 70%,#f1eeea 100%)}
.slide-caption{left:5px;top:70px;width:436px;height:43px;background:rgba(255,255,255,.55);font-family:"Questrial",sans-serif;font-size:30px;line-height:43px;padding-left:12px;color:#111;letter-spacing:.5px;white-space:nowrap}
.slide-arrow{top:140px;width:32px;height:58px;background:rgba(255,255,255,.85);display:flex;align-items:center;justify-content:center}
.slide-arrow.prev{left:0;border-radius:0 29px 29px 0}
.slide-arrow.next{right:0;border-radius:29px 0 0 29px}

/* welcome */
.welcome-title{left:116px;top:622px;font-family:"Questrial",sans-serif;font-size:30px;color:var(--title);display:flex;align-items:center;gap:12px;white-space:nowrap}
.welcome-title .brand-inline{color:#555;font-size:17px;line-height:19px}
.appointment-btn{left:668px;top:614px;width:247px;height:51px;border-radius:26px;background:linear-gradient(#c7e26a,#8cbf24 60%,#79ab18);box-shadow:0 3px 4px rgba(0,0,0,.25),inset 0 0 0 2px #6f9f16;display:flex;align-items:center;justify-content:center;gap:8px;font-family:"Open Sans",sans-serif;font-weight:700;font-size:19px;letter-spacing:-.3px;color:var(--navy-deep);white-space:nowrap}
.appointment-btn svg{flex:none}
.welcome-rule{left:119px;top:676px;width:799px;height:1px;background:#d6d6d6}
.intro{left:117px;top:692px;width:806px;font-size:11.6px;line-height:17.3px;color:var(--text)}
.intro p+p{margin-top:17px}

/* columns */
.col-title{font-family:"Questrial",sans-serif;font-size:24px;color:var(--title);white-space:nowrap}
.col-frame{width:230px;height:105px;background:#dcdcdc;padding:8px}
.col-img{width:100%;height:100%;border:1px solid #fff}
.col-text{width:232px;font-size:10.6px;line-height:16.5px;color:var(--text)}
.learn-more{font-size:10px;font-style:italic;color:var(--green-dark);text-align:right;width:228px}
.col-divider{width:1px;height:224px;background:#d4d4d4;top:860px}
.testimonial h4{font-family:"Open Sans",sans-serif;font-weight:600;font-size:11.4px;color:#111;letter-spacing:.1px;white-space:nowrap}
.stars{display:flex;gap:2px;margin:4px 0 3px}
.testimonial .date{font-size:10px;font-style:italic;color:var(--green-dark)}
.testimonial p{font-size:10.4px;line-height:11.8px;color:#222;margin-top:5px;width:226px}
.testimonial-rule{width:227px;height:1px;background:#dcdcdc}

/* footer */
.site-footer{left:0;top:1107px;width:1029px;height:93px;background:linear-gradient(#2a2a2a,#161616)}
.footer-brand{left:122px;top:21px;display:flex;align-items:center;gap:10px}
.footer-brand .brand-name{font-size:20px;line-height:22px;color:#e8e8e8}
.footer-brand .brand-dot{width:11px;height:11px;background:#9a9a9a}
.talk{left:334px;top:18px;display:flex;align-items:center;gap:10px;font-family:"Questrial",sans-serif;color:var(--footer-text);white-space:nowrap}
.talk .label{font-size:17px}
.talk .phone{font-size:34px;letter-spacing:-.5px}
.footer-rule{left:334px;top:55px;width:402px;border-top:1px dotted #555}
.legal{left:337px;top:71px;font-size:10px;color:var(--footer-text);letter-spacing:.3px;white-space:nowrap}
.legal span{margin:0 4px}
.social{left:798px;top:33px;display:flex;gap:3px}
.social span{width:28px;height:28px;border-radius:50%;background:linear-gradient(#bdbdbd,#8a8a8a)}
</style>
</head>
<body>

<header class="site-header abs">
  <div class="brand abs"><span class="brand-dot"></span><div class="brand-name">Tamsin Vale<br>Chiropractic</div></div>
  <div class="header-photo abs" role="img" aria-label="Smiling family of four: father, mother and two young children"></div>
</header>

<nav class="main-nav abs">
  <ul>
    <li class="active">Home</li>
    <li>About Us</li>
    <li>Contact Us</li>
    <li>Services</li>
    <li>Testimonials</li>
  </ul>
</nav>

<section class="slider abs">
  <div class="slide-photo abs" role="img" aria-label="Chiropractor adjusting a patient's lower back in the clinic"></div>
  <div class="slide-caption abs">Restoring Health To Your Body</div>
  <div class="slide-arrow prev abs"><svg width="10" height="16" viewBox="0 0 10 16"><path d="M8 1 2 8l6 7" fill="none" stroke="#0e3a6b" stroke-width="3"/></svg></div>
  <div class="slide-arrow next abs"><svg width="10" height="16" viewBox="0 0 10 16"><path d="M2 1l6 7-6 7" fill="none" stroke="#0e3a6b" stroke-width="3"/></svg></div>
</section>

<div class="welcome-title abs">WELCOME TO <span class="brand-inline">Tamsin Vale<br>Chiropractic</span></div>
<div class="appointment-btn abs"><span>Click Appointment</span>
  <svg width="26" height="26" viewBox="0 0 26 26"><circle cx="13" cy="13" r="12" fill="#6e9c18" stroke="#d7ec9a" stroke-width="1.5"/><path d="M7 13h11M14 8l5 5-5 5" fill="none" stroke="#e9f5c8" stroke-width="2"/></svg>
</div>
<div class="welcome-rule abs"></div>

<div class="intro abs">
  <p>simply dummy text of the printing and typesetting industry. Lorem Ipsum has been the industry's standard dummy text ever since the 1500s, when an unknown printer took a galley of type and scrambled it to make a type specimen book. It has survived not only five centuries, but also the leap into electronic typesetting, remaining essentially unchanged. It was popularised in the 1960s with the release of standard dummy text ever since the 1500s, when an unknown printer took a galley of type and scrambled it to make a type specimen book.</p>
  <p>It has survived since the 1500s, when an unknown printer took a galley of type and scrambled it to make a type not only five centuries, but also the leap into electronic typesetting, remaining essentially unchanged. It was popularised Letraset sheets containing Lorem Ipsum passages.</p>
</div>

<!-- services -->
<h3 class="col-title abs" style="left:119px;top:854px">Our Services</h3>
<div class="col-frame abs" style="left:119px;top:893px"><div class="col-img" role="img" aria-label="Hands treating a patient's back" style="background:linear-gradient(90deg,#c99c82,#e7cdbd 60%,#f1e4dc)"></div></div>
<p class="col-text abs" style="left:120px;top:1009px">simply dummy text of the printing and typesetting industry. Lorem Ipsum has been the industry's standard dummy text ever since.</p>
<div class="learn-more abs" style="left:119px;top:1063px">Learn More »</div>
<div class="col-divider abs" style="left:373px"></div>

<!-- products -->
<h3 class="col-title abs" style="left:399px;top:854px">Our Products</h3>
<div class="col-frame abs" style="left:399px;top:893px"><div class="col-img" role="img" aria-label="Chiropractic adjustment table" style="background:linear-gradient(160deg,#fff 20%,#5a5f63 45%,#2b2f33 55%,#e6e0d8 80%,#fff)"></div></div>
<p class="col-text abs" style="left:400px;top:1009px">simply dummy text of the printing and typesetting industry. Lorem Ipsum has been the industry's standard dummy text ever since.</p>
<div class="learn-more abs" style="left:399px;top:1063px">Learn More »</div>
<div class="col-divider abs" style="left:651px"></div>

<!-- testimonials -->
<h3 class="col-title abs" style="left:674px;top:856px">Clients Testimonials</h3>
<div class="testimonial abs" style="left:676px;top:896px">
  <h4>SIMPLY TEXT DUMMY TEXT THE PRINTING</h4>
  <div class="stars">
    <svg width="68" height="12" viewBox="0 0 68 12"><g fill="var(--star)"><path id="st" d="M6 0l1.8 3.9 4.2.4-3.2 2.8 1 4.1L6 9.1 2.2 11.2l1-4.1L0 4.3l4.2-.4z"/><use href="#st" x="14"/><use href="#st" x="28"/><use href="#st" x="42"/><use href="#st" x="56"/></g></svg>
  </div>
  <div class="date">Wed, May 12, 2013</div>
  <p>simply dummy text of the printing and type sett ing Ipsum has industry....</p>
</div>
<div class="testimonial-rule abs" style="left:676px;top:982px"></div>
<div class="testimonial abs" style="left:676px;top:991px">
  <h4>SIMPLY TEXT DUMMY TEXT THE PRINTING</h4>
  <div class="stars">
    <svg width="68" height="12" viewBox="0 0 68 12"><g fill="var(--star)"><use href="#st"/><use href="#st" x="14"/><use href="#st" x="28"/><use href="#st" x="42"/><use href="#st" x="56"/></g></svg>
  </div>
  <div class="date">Wed, May 12, 2013</div>
  <p>simply dummy text of the printing and type sett ing Ipsum has industry....</p>
</div>

<footer class="site-footer abs">
  <div class="footer-brand abs"><span class="brand-dot"></span><div class="brand-name">Tamsin Vale<br>Chiropractic</div></div>
  <div class="talk abs"><span class="label">Talk to us!</span>
    <svg width="14" height="26" viewBox="0 0 14 26"><path d="M12 3C6 3 3 8 3 13s3 10 9 10" fill="none" stroke="#8a8a8a" stroke-width="5" stroke-linecap="round"/></svg>
    <span class="phone">800 341 275</span></div>
  <div class="footer-rule abs"></div>
  <div class="legal abs">©2013. All rights reserved. <span></span>Privacy Policy<span>|</span>Terms &amp; Conditions</div>
  <div class="social abs" aria-label="Social links"><span></span><span></span><span></span><span></span></div>
</footer>

</body>
</html>
```